Need a website setup for our new removalist business.
Our business is called Kettle Brook Removals and would like a website setup.
We don’t have a website, logo or design as of yet. Our truck is blue so something possibly that works and can incorporate the blue.

```html
<!DOCTYPE html>
<html lang="en">
<head>
<meta charset="utf-8">
<title>Kettle Brook Removals</title>
<link href="https://fonts.googleapis.com/css2?family=Poppins:wght@400;500;600;700;800;900&display=swap" rel="stylesheet">
<style>
:root{
  --blue:#1d4a9d;
  --navy:#183f8c;
  --yellow:#f9b52d;
  --ink:#111111;
  --grey:#6b6b6b;
  --light:#eef0f3;
  --footer:#111111;
  --white:#ffffff;
}
*{box-sizing:border-box;margin:0;padding:0}
html,body{width:1200px;height:3340px;overflow:hidden}
body{position:relative;font-family:'Poppins',sans-serif;color:var(--ink);background:var(--white)}
.abs{position:absolute}
.btn{position:absolute;display:flex;align-items:center;justify-content:center;gap:8px;font-weight:600;color:var(--white);text-transform:uppercase;letter-spacing:.2px;text-decoration:none}
.btn svg{width:11px;height:11px}
.btn-yellow{background:var(--yellow)}
.btn-blue{background:var(--blue)}

/* hero */
.hero-bg{left:0;top:0;width:1195px;height:573px;background:linear-gradient(100deg,#e9ebee 0%,#dfe2e6 45%,#d3d7dc 100%)}
.brand{display:flex;align-items:center;gap:10px;font-weight:600;color:var(--blue);white-space:nowrap}
.brand-dot{width:16px;height:16px;border-radius:50%;background:var(--yellow);flex:none}
.header-brand{left:62px;top:47px;font-size:19px}
.nav{left:394px;top:62px;display:flex;gap:44px;font-size:14px;font-weight:500;color:var(--ink)}
.hero-title{left:68px;top:164px;font-size:47px;line-height:57px;font-weight:900;color:var(--navy);letter-spacing:-.5px;white-space:nowrap}
.hero-text{left:70px;top:342px;width:345px;font-size:16px;line-height:20px;color:#444}
.hero-visual{left:440px;top:140px;width:722px;height:433px;border-radius:40px 120px 0 0;background:linear-gradient(120deg,#3d7fd0 0%,#1d58b4 55%,#17418a 100%)}

/* quote band */
.quote-band{left:0;top:573px;width:1195px;height:153px;background:var(--blue)}
.quote-tag{left:0;top:573px}
.quote-label{left:28px;top:609px;font-size:31px;line-height:38px;font-weight:700;color:var(--white)}
.field{top:638px;width:155px;height:35px;background:#3a63b0;border:1px solid #5078c0;color:#c8d4ee;font-size:10px;padding:10px 16px}

/* about */
.about-frame{left:170px;top:831px;width:415px;height:413px;border:7px solid var(--yellow)}
.about-photo{left:85px;top:882px;width:408px;height:408px;border-radius:32px;background:linear-gradient(135deg,#c8b49a 0%,#8c98a4 50%,#5a4a3c 100%)}
.eyebrow{font-size:19px;font-weight:500;color:var(--navy)}
.about-eyebrow{left:666px;top:892px}
.about-title{left:666px;top:930px;width:450px;font-size:41px;line-height:47px;font-weight:600}
.about-text{left:666px;top:1092px;width:430px;font-size:19px;line-height:24px;color:var(--grey)}

/* services */
.services-bg{left:4px;top:1408px;width:1196px;height:737px;background:linear-gradient(120deg,#e6e8ee 0%,#f1f2f5 50%,#e3e6ec 100%)}
.center{left:0;width:1200px;text-align:center}
.section-title{font-size:40px;font-weight:600}
.card{top:1605px;width:300px;height:343px;border-radius:32px;background:linear-gradient(160deg,#5a7ccc 0%,#3d62b6 60%,#2f52a4 100%)}
.card-title{position:absolute;left:0;width:100%;top:232px;text-align:center;color:var(--white);font-size:21px;line-height:25px;font-weight:500}
.card .btn{left:50%;transform:translateX(-50%);top:297px;width:108px;height:26px;font-size:10px}
.arrow{width:66px;height:44px}

/* testimonials */
.review{top:2452px;width:429px;height:273px;background:var(--white);box-shadow:0 6px 40px rgba(0,0,0,.08)}
.avatar{position:absolute;left:24px;top:22px;width:62px;height:62px;border-radius:50%;background:linear-gradient(135deg,#8d9aa8,#c9b59c)}
.reviewer{position:absolute;left:106px;top:34px;font-size:14px;font-weight:600;color:var(--navy)}
.stars{position:absolute;left:104px;top:52px;color:var(--yellow);font-size:16px;letter-spacing:2px}
.quote-mark{position:absolute;right:20px;top:28px;width:34px;height:28px}
.review-text{position:absolute;left:31px;top:128px;width:370px;font-size:15.5px;line-height:19px;color:var(--grey)}

/* footer */
.footer{left:4px;top:2870px;width:1196px;height:470px;background:var(--footer)}
.footer-brand{left:107px;top:2990px;font-size:23px;color:var(--white)}
.footer-text{left:108px;top:3078px;width:300px;font-size:13.5px;line-height:21px;color:#c9c9c9}
.social{left:108px;top:3158px;display:flex;gap:18px}
.social span{width:18px;height:18px;border-radius:3px;background:var(--yellow);display:block}
.col-title{top:2987px;font-size:22px;font-weight:500;color:var(--white)}
.links{list-style:none;font-size:14px;color:#c9c9c9}
.links li{display:flex;align-items:center;gap:8px;height:31.5px;white-space:nowrap}
.links svg{width:14px;height:10px;flex:none}
.contact li svg{width:13px;height:13px}
.legal{top:3298px;font-size:12px;color:#bdbdbd}
</style>
</head>
<body>

<!-- hero -->
<div class="abs hero-bg" role="img" aria-label="Softly faded photo of a street with a removal van being loaded"></div>
<div class="abs brand header-brand"><span class="brand-dot"></span>Kettle Brook Removals</div>
<nav class="abs nav"><span>HOME</span><span>ABOUT</span><span>SERVICES</span><span>PRICING</span><span>TESTIMONIALS</span></nav>
<a class="btn btn-blue" style="left:1004px;top:57px;width:120px;height:30px;font-size:10.5px">Get a quote <svg viewBox="0 0 10 10"><path d="M2 8L8 2M3 2h5v5" stroke="#fff" stroke-width="1.4" fill="none"/></svg></a>
<div class="abs hero-visual" role="img" aria-label="Blue removal van with a mover in overalls carrying a cardboard box"></div>
<h1 class="abs hero-title">Moving Every<br>Customer<br>With Care</h1>
<p class="abs hero-text">Lorem ipsum dolor sit amet, consectetuer adipiscing elit. Aenean commodo ligula eget dolor.</p>
<a class="btn btn-yellow" style="left:69px;top:424px;width:119px;height:30px;font-size:10.5px">Get a quote <svg viewBox="0 0 10 10"><path d="M2 8L8 2M3 2h5v5" stroke="#fff" stroke-width="1.4" fill="none"/></svg></a>
<a class="btn btn-blue" style="left:204px;top:424px;width:120px;height:30px;font-size:10.5px">Our services <svg viewBox="0 0 10 10"><path d="M2 8L8 2M3 2h5v5" stroke="#fff" stroke-width="1.4" fill="none"/></svg></a>

<!-- request quote -->
<div class="abs quote-band"></div>
<svg class="abs quote-tag" width="232" height="153" viewBox="0 0 232 153"><path d="M0 0H130L230 76.5L130 153H0Z" fill="#f9b52d"/></svg>
<h2 class="abs quote-label">Request<br>Quote</h2>
<div class="abs field" style="left:289px">Name</div>
<div class="abs field" style="left:459px">Email</div>
<div class="abs field" style="left:629px">Phone</div>
<div class="abs field" style="left:800px">Select Service</div>
<a class="btn btn-yellow" style="left:990px;top:641px;width:120px;height:30px;font-size:10.5px">Get a quote <svg viewBox="0 0 10 10"><path d="M2 8L8 2M3 2h5v5" stroke="#fff" stroke-width="1.4" fill="none"/></svg></a>

<!-- about -->
<div class="abs about-frame"></div>
<div class="abs about-photo" role="img" aria-label="Smiling mover handing a cardboard box from a van"></div>
<p class="abs eyebrow about-eyebrow">About Us</p>
<h2 class="abs about-title">We are Your Partner to Moving Across Everywhere.</h2>
<p class="abs about-text">LLorem ipsum dolor sit amet, consectetur adipiscing elit. Ut elit tellus, luctus nec ullamcorper mattis, pulvinar dapibus leo.</p>
<a class="btn btn-yellow" style="left:666px;top:1198px;width:184px;height:47px;font-size:18px">Get a quote <svg viewBox="0 0 10 10" style="width:14px;height:14px"><path d="M2 8L8 2M3 2h5v5" stroke="#fff" stroke-width="1.3" fill="none"/></svg></a>

<!-- services -->
<div class="abs services-bg" role="img" aria-label="Faded background photo of movers loading boxes"></div>
<p class="abs eyebrow center" style="top:1470px">What we DO</p>
<h2 class="abs section-title center" style="top:1503px">Services We Offer</h2>
<svg class="abs arrow" style="left:35px;top:1771px" viewBox="0 0 66 44"><circle cx="42" cy="22" r="20" fill="#f6dca6"/><path d="M56 22H6M20 8L6 22l14 14" stroke="#4a6db6" stroke-width="4" fill="none" stroke-linecap="round" stroke-linejoin="round"/></svg>
<svg class="abs arrow" style="left:1095px;top:1771px" viewBox="0 0 66 44"><circle cx="24" cy="22" r="20" fill="#f6dca6"/><path d="M10 22H60M46 8l14 14-14 14" stroke="#4a6db6" stroke-width="4" fill="none" stroke-linecap="round" stroke-linejoin="round"/></svg>
<div class="abs card" style="left:118px" role="img" aria-label="Movers loading boxes into a van">
  <p class="card-title">Long Distance<br>Moving</p>
  <a class="btn btn-yellow">Learn more <svg viewBox="0 0 10 10"><path d="M2 8L8 2M3 2h5v5" stroke="#fff" stroke-width="1.4" fill="none"/></svg></a>
</div>
<div class="abs card" style="left:445px" role="img" aria-label="Two movers lifting a box from a van">
  <p class="card-title">Local Moving</p>
  <a class="btn btn-yellow">Learn more <svg viewBox="0 0 10 10"><path d="M2 8L8 2M3 2h5v5" stroke="#fff" stroke-width="1.4" fill="none"/></svg></a>
</div>
<div class="abs card" style="left:772px" role="img" aria-label="Mover packing boxes in a living room">
  <p class="card-title">Packing and<br>Unpacking</p>
  <a class="btn btn-yellow">Learn more <svg viewBox="0 0 10 10"><path d="M2 8L8 2M3 2h5v5" stroke="#fff" stroke-width="1.4" fill="none"/></svg></a>
</div>
<a class="btn btn-blue" style="left:503px;top:2025px;width:184px;height:47px;font-size:18px">Get a quote <svg viewBox="0 0 10 10" style="width:14px;height:14px"><path d="M2 8L8 2M3 2h5v5" stroke="#fff" stroke-width="1.3" fill="none"/></svg></a>

<!-- testimonials -->
<p class="abs eyebrow center" style="top:2246px">Testimonials</p>
<h2 class="abs section-title center" style="top:2283px;font-size:42px">What Client Says</h2>
<svg class="abs arrow" style="left:35px;top:2563px" viewBox="0 0 66 44"><circle cx="42" cy="22" r="20" fill="#f6dca6"/><path d="M56 22H6M20 8L6 22l14 14" stroke="#4a6db6" stroke-width="4" fill="none" stroke-linecap="round" stroke-linejoin="round"/></svg>
<svg class="abs arrow" style="left:1095px;top:2563px" viewBox="0 0 66 44"><circle cx="24" cy="22" r="20" fill="#f6dca6"/><path d="M10 22H60M46 8l14 14-14 14" stroke="#4a6db6" stroke-width="4" fill="none" stroke-linecap="round" stroke-linejoin="round"/></svg>
<div class="abs review" style="left:131px">
  <div class="avatar" role="img" aria-label="Client portrait"></div>
  <p class="reviewer">Daniel R.</p>
  <p class="stars">★★★★★</p>
  <svg class="quote-mark" viewBox="0 0 34 28"><path d="M2 2h12v12l-6 12H3l5-12H2zM19 2h12v12l-6 12h-5l5-12h-6z" fill="#4a6db6"/></svg>
  <p class="review-text">Lorem ipsum dolor sit amet, consectetuer adipiscing elit. Aenean commodo ligula eget dolor.Aenean massa. Cum sociis natoque penatibus et magnis dis parturient montes, nascetur ridiculus mus.</p>
</div>
<div class="abs review" style="left:617px">
  <div class="avatar" role="img" aria-label="Client portrait"></div>
  <p class="reviewer">Daniel R.</p>
  <p class="stars">★★★★★</p>
  <svg class="quote-mark" viewBox="0 0 34 28"><path d="M2 2h12v12l-6 12H3l5-12H2zM19 2h12v12l-6 12h-5l5-12h-6z" fill="#4a6db6"/></svg>
  <p class="review-text">Lorem ipsum dolor sit amet, consectetuer adipiscing elit. Aenean commodo ligula eget dolor.Aenean massa. Cum sociis natoque penatibus et magnis dis parturient montes, nascetur ridiculus mus.</p>
</div>

<!-- footer -->
<footer class="abs footer"></footer>
<div class="abs brand footer-brand"><span class="brand-dot" style="width:20px;height:20px"></span>Kettle Brook Removals</div>
<p class="abs footer-text">Lorem ipsum dolor sit amet, consectetuer adipiscing elit. Aenean commodo ligula eget dolor. Aenean massa.</p>
<div class="abs social"><span></span><span></span><span></span></div>

<h3 class="abs col-title" style="left:492px">Quick Links</h3>
<ul class="abs links" style="left:500px;top:3039px">
  <li><svg viewBox="0 0 14 10"><path d="M1 5h11M8 1l4 4-4 4" stroke="#f9b52d" stroke-width="1.5" fill="none"/></svg>Home</li>
  <li><svg viewBox="0 0 14 10"><path d="M1 5h11M8 1l4 4-4 4" stroke="#f9b52d" stroke-width="1.5" fill="none"/></svg>About</li>
  <li><svg viewBox="0 0 14 10"><path d="M1 5h11M8 1l4 4-4 4" stroke="#f9b52d" stroke-width="1.5" fill="none"/></svg>Services</li>
  <li><svg viewBox="0 0 14 10"><path d="M1 5h11M8 1l4 4-4 4" stroke="#f9b52d" stroke-width="1.5" fill="none"/></svg>Pricing</li>
  <li><svg viewBox="0 0 14 10"><path d="M1 5h11M8 1l4 4-4 4" stroke="#f9b52d" stroke-width="1.5" fill="none"/></svg>Contact</li>
</ul>

<h3 class="abs col-title" style="left:705px">Services</h3>
<ul class="abs links" style="left:712px;top:3044px">
  <li><svg viewBox="0 0 14 10"><path d="M1 5h11M8 1l4 4-4 4" stroke="#f9b52d" stroke-width="1.5" fill="none"/></svg>Local Moving</li>
  <li><svg viewBox="0 0 14 10"><path d="M1 5h11M8 1l4 4-4 4" stroke="#f9b52d" stroke-width="1.5" fill="none"/></svg>Commercial Moving</li>
  <li><svg viewBox="0 0 14 10"><path d="M1 5h11M8 1l4 4-4 4" stroke="#f9b52d" stroke-width="1.5" fill="none"/></svg>Military Moving</li>
  <li><svg viewBox="0 0 14 10"><path d="M1 5h11M8 1l4 4-4 4" stroke="#f9b52d" stroke-width="1.5" fill="none"/></svg>StorageSolutions</li>
  <li><svg viewBox="0 0 14 10"><path d="M1 5h11M8 1l4 4-4 4" stroke="#f9b52d" stroke-width="1.5" fill="none"/></svg>Truck Rental</li>
</ul>

<h3 class="abs col-title" style="left:922px">Contact us</h3>
<ul class="abs links contact" style="left:928px;top:3047px;font-size:13px;color:#e0e0e0">
  <li><svg viewBox="0 0 13 13"><path d="M3 1l2 3-1.5 1.5c.8 1.7 2.3 3.2 4 4L9 8l3 2-1 2.5C6 12 1 7 .5 2z" fill="#f9b52d"/></svg>(02) 5550 1842</li>
  <li><svg viewBox="0 0 13 13"><rect x="1" y="3" width="11" height="8" fill="#f9b52d"/><path d="M1 3l5.5 4L12 3" stroke="#111" stroke-width="1" fill="none"/></svg>hello@kettlebrook.example</li>
  <li><svg viewBox="0 0 13 13"><path d="M6.5 12S2 7.5 2 5a4.5 4.5 0 019 0c0 2.5-4.5 7-4.5 7z" fill="#f9b52d"/></svg>12 Willow Lane, Brookdale</li>
</ul>

<p class="abs legal" style="left:119px">Copyright © 2024 Kettle Brook Removals. All Rights Reserved.</p>
<p class="abs legal" style="left:861px">Terms &amp; Conditions | &nbsp;Privacy Policy</p>

</body>
</html>
```